Looking for an amazing business card for a thriving DJ business

We need a business card design for a DJ company based in South Florida. The DJ company specializes in weddings, parties, bar mitzvahs, corporate events, proms, and reunions. We are looking for a modern, simple business card design. The card should state DJ Marlow K.
Updates

The name on the card should be DJ Marlow K

Industry/Entity Type

Entertainment Industry

Contact Information for Business Card

DJ Marlow K
512.447.2086
atxdjmarlowk@quellmail.com
https://www.facebook.com/DjMarlowK/
https://www.instagram.com/djmarlow.k/
www.djmarlowk.net

Font styles to use
Serif
Sans Serif

Requirements
Must have
• My business card has to be awesome.
Should not have
• The card has to have personality.

```html
<!DOCTYPE html>
<html lang="en">
<head>
<meta charset="utf-8">
<title>DJ Marlow K — Business Card</title>
<link rel="stylesheet" href="https://fonts.googleapis.com/css2?family=Montserrat:wght@700&family=Questrial&display=swap">
<style>
  :root {
    --page: #2b2b2e;
    --card: #0b0c30;
    --card-edge: #05061c;
    --ink: #ffffff;
  }
  * { margin: 0; padding: 0; box-sizing: border-box; }
  html, body { width: 1200px; height: 800px; overflow: hidden; background: var(--page); }
  .stage { position: relative; width: 1200px; height: 800px; }
  .card {
    position: absolute;
    width: 560px; height: 320px;
    background: linear-gradient(135deg, var(--card) 0%, var(--card-edge) 100%);
    overflow: hidden;
    color: var(--ink);
  }
  .card-front { left: 250px; top: 60px; }
  .card-back { left: 390px; top: 420px; }

  .front-mark {
    position: absolute; left: 60px; top: 70px;
    width: 180px; height: 180px;
    border: 2px solid var(--ink); border-radius: 50%;
  }
  .front-initials {
    position: absolute; left: 268px; top: 78px;
    font-family: "Montserrat", sans-serif; font-weight: 700;
    font-size: 128px; line-height: 128px; letter-spacing: -2px;
    white-space: nowrap;
  }
  .front-name {
    position: absolute; left: 466px; top: 90px;
    writing-mode: vertical-rl; transform: rotate(180deg);
    font-family: "Montserrat", sans-serif; font-weight: 700;
    font-size: 22px; letter-spacing: 1px; white-space: nowrap;
  }

  .back-arc { position: absolute; left: 0; top: 0; }
  .back-name {
    position: absolute; left: 250px; top: 100px;
    font-family: "Montserrat", sans-serif; font-weight: 700;
    font-size: 30px; letter-spacing: 1px; white-space: nowrap;
  }
  .contact-list {
    position: absolute; left: 250px; top: 152px;
    list-style: none;
    font-family: "Questrial", sans-serif; font-size: 15px; line-height: 25px;
  }
  .contact-item { display: flex; align-items: center; gap: 10px; }
  .contact-icon { width: 14px; height: 14px; flex: none; }
</style>
</head>
<body>
<main class="stage">
  <section class="card card-front" aria-label="Card front">
    <div class="front-mark"></div>
    <div class="front-initials">DJ</div>
    <div class="front-name">MARLOW K</div>
  </section>

  <section class="card card-back" aria-label="Card back">
    <svg class="back-arc" width="560" height="320" viewBox="0 0 560 320" aria-hidden="true">
      <circle cx="20" cy="190" r="190" fill="none" stroke="#ffffff" stroke-width="2"/>
    </svg>
    <h1 class="back-name">DJ MARLOW K</h1>
    <ul class="contact-list">
      <li class="contact-item">
        <svg class="contact-icon" viewBox="0 0 14 14" aria-hidden="true"><path d="M3 1l2.5 3-1.5 1.5c.8 1.8 2.2 3.2 4 4L9.5 8 13 10.5 11.5 13C6 12.5 1.5 8 1 2.5z" fill="#fff"/></svg>
        <span>512 447 2086</span>
      </li>
      <li class="contact-item">
        <svg class="contact-icon" viewBox="0 0 14 14" aria-hidden="true"><rect x="1" y="3" width="12" height="8" fill="none" stroke="#fff" stroke-width="1.4"/><path d="M1 3l6 5 6-5" fill="none" stroke="#fff" stroke-width="1.4"/></svg>
        <span>atxdjmarlowk@quellmail.com</span>
      </li>
      <li class="contact-item">
        <svg class="contact-icon" viewBox="0 0 14 14" aria-hidden="true"><rect x="1.5" y="1.5" width="11" height="11" fill="#fff"/></svg>
        <span>/DjMarlowK/</span>
      </li>
      <li class="contact-item">
        <svg class="contact-icon" viewBox="0 0 14 14" aria-hidden="true"><rect x="1.5" y="1.5" width="11" height="11" fill="none" stroke="#fff" stroke-width="1.4"/></svg>
        <span>/djmarlow.k/</span>
      </li>
      <li class="contact-item">
        <svg class="contact-icon" viewBox="0 0 14 14" aria-hidden="true"><circle cx="7" cy="7" r="6" fill="none" stroke="#fff" stroke-width="1.3"/><ellipse cx="7" cy="7" rx="2.6" ry="6" fill="none" stroke="#fff" stroke-width="1.1"/><path d="M1 7h12" stroke="#fff" stroke-width="1.1"/></svg>
        <span>www.djmarlowk.net</span>
      </li>
    </ul>
  </section>
</main>
</body>
</html>
```